Commercial Cleaning Company specializing in windows and floors

Looking to have a brochure made for commercial cleaning company. Services include 2 categories:
1. Window Washing

2. Floor Cleaning and Restoration.

Within floor and cleaning restoration, there are several categories:
Carpet Cleaning & Restoration
-Tile and Grout Cleaning & Restoration
-Concrete Cleaning & Restoration
-Stone Cleaning & Restoration (Terrazzo, Marble, Limestone)
-VCT Cleaning & Restoration
-Wood Floor Cleaning & Restoration
-Epoxy Floor Cleaning & Restoration
Floor cleaning Text:
FLOOR CARE:

CARPET FLOORS
Low Moisture, Safe & Fast <--- Increase Font and color
Designed to support a healthy indoor environment, our carpet cleaning methods will eliminate the most common problems caused by other cleaning methods that lead to mold growth, mildew, volatile organic compounds (VOC), insufficient drying times, recurring stains and safety hazards. We also mitigate common safety hazards associated with multiple lengthy hoses, insecure open doors, and slippery hard surfaces. You'll find our system also eliminates both noise and emission pollution around your facility during cleaning times that are common with other cleaning methods.
Our low-moisture system supports a healthy indoor environment so carpets will stay clean & vibrant in color. With superior drying times, our methods eliminates mold growth and mildew. When we are finished cleaning, all that’s left are incredibly clean and fresh smelling carpets

TILE & GROUT FLOORS
We get deep into our cleaning <--- Increase Font and color
Tile and Grout floors can be very difficult to maintain. Often, dirt and grime get trapped in grout lines and crevices and discolor them, making the floors appear dirty. Our company has done all the experimenting for you, and we know the correct brushes, weight kits, machines, and chemical combinations to use to restore and maintain these types of floors, without leaving residue behind that will cause soil to return.

CONCRETE FLOORS
Pores & Crevices are no match <--- Increase Font and color
When it comes to scrubbing and cleaning concrete surfaces such as school hallways, patios, and other types of high traffic concrete flooring, we have you covered.
We're here to keep your employees and visitors safer. We eliminate having to use harsh chemicals and abundances of water to remove the heavy soil that has settled deep down in the concrete pores and crevices.

STONE FLOORS - TERRAZZO, MARBLE, LIMESTONE
We are experts in protecting your major flooring investment. <--- Increase Font and color
If you have high end stone floors, make sure they are performing their best for your facility. We can make educated recommendations on restoration schedules, cleaning methods, schedules, matting and everything related to making your floors "pop". These multi-step processes can be complex, but our experience ensures the best result for your building.

WOOD FLOORS
Wood floors can be tricky - We know how to clean and refinish them. <--- Increase Font and color
If you aren't careful, you may end up with undesirable results when dealing with wood floors. Traditional swing machines can leave swirls if not used correctly, and other methods may damage the wood. We've trained with leading wood floor companies to ensure a process that's safe for your floors and bring you the results you're looking for.

EPOXY FLOORS
We Clean Terrazzo, Flake coating, Screeds & More <--- Increase Font and color

Epoxy is protected from chemicals, dirt, liquids and other contaminants, however, Epoxy floors need to be cleaned routinely as they lose their original luster. We can restore any type of Epoxy floor and bring them back to life.

VCT/VINYL FLOORS <--- Increase Font and color

The most common floor types are our specialty
We can assist you in the maintenance of VCT and vinyl floors. We are helpful resources for assistance with stripping and re coating, daily maintenance, burnishing, and restorative buffing. We have worked with major pad manufacturers and chemical companies to help make selections on the best possible floor maintenance system for these common floors.

Window cleaning Text:
WINDOW CARE:
Our goal is to leave your employees and visitors with the best possible impression of your facility, and clean windows are a huge part of that. BrightHollow uses the latest pure water technology and equipment to leave your windows sparkling clean. We are trained to identify the correct process for various interior and exterior windows, as well as performing restorative processes for things like hard water deposits.
Older cleaning methods often leave behind streaking or residues. Brighthollow has invested in equipment that utilizes de-ionized water, microfibers, and state of the art filtration. Recent designs in pole construction allow us to access hard to reach windows, facades, solar panels, sills, and ledges without the use of heavy equipment.
We offer a spate of maintenance programs the ensure the lowest total cost of cleaning. Inquire with us to learn more about why contracting these important cleaning tasks to Brighthollows will relieve you of: equipment storage and maintenance , brush selection, filtration concerns - as well as the liability of work that can sometimes present danger to untrained employees.

Company Biography Page:

BrightHollow is a family based company located in the greater Houston area that specializes in commercial floor care and window cleaning. Our mission is to prioritize the health and safety of the people who use your building by offering cleaning methods that are safe and use the latest industry technology. We understand that a clean, well maintained building has a direct relationship with your image - and that can have a direct effect on your bottom line or reputation. Please consider us for further consultation if you are interested in a no obligation discussion about your facility.

The management of BrightHollow has spent their entire professional lives in the commercial cleaning industry. We have recently sold facility supply distribution company and understand the facility maintenance industry top to bottom. In that time, we've met with innumerable manufacturers, distributors, trade groups, trainers and end users to gain insight into national and regional cleaning trends and methods. We understand budgets, compliance requirements, workflow timelines, and restorative schedules that you don't typically find in a contract cleaning company.
We are confident you will benefit from our wide range of experience and expertise when it comes to maintaining your facility.

Layout:

I think it would work best to have a 4 page single fold booklet type brochure - but open to any suggestions.
The inside would have the 2 services - one side hard floors and the other side windows. Either the front or the back would have our biography on it (probably the back?).
I will give you more input like the address and phone number at the end, it can be added easily.

For the pictures I've added:
The ones that include the word "example" are to be used when incorporating the services.

I've also included a bunch of window pictures. You can use some or none of these (and get other ones) in companion with the text about window cleaning.

Target Market(s)

Commercial buildings and institutions looking for our specific cleaning services

Industry/Entity Type

Commercial Cleaning

Font styles to use
Serif
Sans Serif

Colors
0054AA
0677BA
7BADD7
CADEEF
E8F1F8
0094D4
00A9DD
6FCCEA
C7EBF8
E9F6FB
59FF00
82FF00
B8FF75
E3FFCB
F4FFEA

Requirements
Must have
• All of the included text (can be edited slightly)
Nice to have
• Additional images or text gleened from other sources or past experience that help communicate our business

```html
<!DOCTYPE html>
<html lang="en">
<head>
<meta charset="utf-8">
<title>BrightHollow – Window and Floor Care Brochure</title>
<link href="https://fonts.googleapis.com/css2?family=Inter:wght@500;600;700&family=Poppins:ital,wght@0,500;0,800;1,800&display=swap" rel="stylesheet">
<style>
  :root{
    --page-bg:#e4e4e4;
    --bio-blue:#0a92d1;
    --brand-blue:#1a78c2;
    --wave-light:#1ba0dc;
    --wave-dark:#1577c2;
    --headline-blue:#0a8ad2;
    --green-dark:#78c20f;
    --green-light:#a3e01a;
    --headline-green:#6dbb3a;
    --white:#ffffff;
  }
  *{margin:0;padding:0;box-sizing:border-box}
  html,body{width:1200px;height:1200px;overflow:hidden;background:var(--page-bg)}
  .spread{position:absolute;left:38px;top:188px;width:1121px;height:793px;display:flex;box-shadow:0 2px 6px rgba(0,0,0,.12)}
  /* back page: biography */
  .bio-page{position:relative;width:560px;height:100%;background:var(--bio-blue);color:var(--white);font-family:'Inter',sans-serif}
  .bio-brand{position:absolute;left:0;right:0;top:232px;text-align:center;font-family:'Poppins',sans-serif;font-weight:500;font-size:34px;letter-spacing:.3px}
  .bio-text{position:absolute;left:34px;width:493px;top:291px}
  .bio-text p{font-size:9.4px;font-weight:600;line-height:14.1px;text-align:justify;text-align-last:center;margin-bottom:8.5px}
  .bio-text p.bio-closing{font-size:12.4px;line-height:14.2px;margin-top:3px}
  .page-url{position:absolute;font-family:'Inter',sans-serif;font-weight:600;font-size:12px;color:var(--white)}
  .bio-page .page-url{left:0;right:0;top:746px;text-align:center}
  /* front page: cover */
  .cover-page{position:relative;width:561px;height:100%;overflow:hidden}
  .cover-art{position:absolute;inset:0}
  .cover-brand{position:absolute;left:60px;top:80px;font-family:'Poppins',sans-serif;font-weight:500;font-size:28px;color:var(--headline-blue)}
  .headline{position:absolute;left:33px;top:330px;font-family:'Poppins',sans-serif;font-weight:800;font-size:45px;line-height:39.5px;letter-spacing:-1.5px}
  .headline span{display:block}
  .headline .blue{color:var(--headline-blue);font-style:italic}
  .headline .green{color:var(--headline-green)}
  .photo{position:absolute;width:246px;height:246px;border-radius:50%;left:280px}
  .photo-window{top:158px;border:3px solid var(--green-dark);background:radial-gradient(circle at 60% 30%,#4d6e3e 0%,#8aa192 45%,#c5d3d8 80%,#a9bcc4 100%)}
  .photo-floor{top:414px;border:3px solid var(--brand-blue);background:linear-gradient(180deg,#7a4a2c 0%,#b98a62 30%,#e2c5a3 60%,#c79a72 100%)}
  .phone-badge{position:absolute;left:206px;top:637px;width:42px;height:42px;border-radius:50%;background:var(--white);display:flex;align-items:center;justify-content:center}
  .phone-number{position:absolute;left:35px;top:675px;font-family:'Inter',sans-serif;font-weight:700;font-size:26.5px;color:var(--white);letter-spacing:.3px}
  .address{position:absolute;left:34px;top:730px;display:flex;gap:10px;font-family:'Inter',sans-serif;font-weight:600;font-size:12.5px;line-height:15px;color:var(--white)}
  .cover-page .page-url{left:374px;top:747px}
</style>
</head>
<body>
<main class="spread">
  <section class="bio-page">
    <div class="bio-brand">BrightHollow</div>
    <div class="bio-text">
      <p>BrightHollow is a family based company located in the greater Houston area that specializes in commercial floor care and window cleaning. Our mission is to prioritize the health and safety of the people who use your building by offering cleaning methods that are safe and use the latest industry technology. We understand that a clean, well maintained building has a direct relationship with your image - and that can have a direct effect on your bottom line or reputation. Please consider us for further consultation if you are interested in a no obligation discussion about your facility.</p>
      <p>The management of BrightHollow has spent their entire professional lives in the commercial cleaning industry. We have recently sold facility supply distribution company and understand the facility maintenance industry top to bottom. In that time, we’ve met with innumerable manufacturers, distributors, trade groups, trainers and end users to gain insight into national and regional cleaning trends and methods. We understand budgets, compliance requirements, workflow timelines, and restorative schedules that you don’t typically find in a contract cleaning company.</p>
      <p class="bio-closing">We are confident you will benefit from our wide range of experience and expertise when it comes to maintaining your facility.</p>
    </div>
    <div class="page-url">www.brighthollow.com</div>
  </section>

  <section class="cover-page">
    <svg class="cover-art" viewBox="0 0 561 793" width="561" height="793" aria-hidden="true">
      <rect x="0" y="0" width="561" height="537" fill="var(--green-dark)"/>
      <rect x="0" y="537" width="561" height="256" fill="var(--brand-blue)"/>
      <rect x="7" y="7" width="547" height="786" fill="var(--white)"/>
      <path d="M7 141 C60 165 80 205 110 200 C230 190 330 100 450 95 C500 92 535 105 554 118 L554 130 C520 115 470 108 420 125 C300 165 230 245 110 240 C60 238 30 215 7 195 Z" fill="var(--green-light)"/>
      <path d="M7 141 C60 165 90 190 130 186 C250 175 340 95 450 90 C500 88 535 100 554 112 L554 125 C515 108 460 104 410 122 C310 158 230 200 130 205 C80 207 40 190 7 175 Z" fill="var(--green-dark)"/>
      <path d="M321 163 C380 135 430 120 470 122 C500 124 520 140 529 156 C500 138 470 132 440 134 C400 137 360 150 321 163 Z" fill="var(--green-dark)"/>
      <path d="M7 643 C40 620 80 608 120 610 C220 615 320 700 400 720 C460 735 520 712 554 680 L554 793 L7 793 Z" fill="var(--wave-light)"/>
      <path d="M7 690 C40 664 80 652 120 652 C220 655 320 715 400 728 C460 738 520 715 554 694 L554 793 L7 793 Z" fill="var(--wave-dark)"/>
      <path d="M326 673 C380 690 440 700 480 695 C510 690 528 680 538 665 C525 695 495 708 460 708 C420 708 370 692 326 673 Z" fill="var(--wave-dark)"/>
    </svg>

    <div class="cover-brand">BrightHollow</div>

    <h1 class="headline">
      <span class="blue">WINDOW</span>
      <span class="green">AND</span>
      <span class="blue">FLOOR</span>
      <span class="green">CARE</span>
    </h1>

    <div class="photo photo-window" role="img" aria-label="Photo of a squeegee wiping a soapy window with trees behind"></div>
    <div class="photo photo-floor" role="img" aria-label="Photo of a polished marble hallway floor in a lobby"></div>

    <div class="phone-badge">
      <svg width="20" height="20" viewBox="0 0 24 24" aria-hidden="true"><path d="M6.6 10.8a15.1 15.1 0 0 0 6.6 6.6l2.2-2.2c.3-.3.7-.4 1-.2 1.1.4 2.3.6 3.6.6.6 0 1 .4 1 1V20c0 .6-.4 1-1 1A17 17 0 0 1 3 4c0-.6.4-1 1-1h3.5c.6 0 1 .4 1 1 0 1.3.2 2.5.6 3.6.1.3 0 .7-.2 1z" fill="var(--brand-blue)"/></svg>
    </div>
    <div class="phone-number">+00 5550 1947</div>

    <div class="address">
      <svg width="20" height="26" viewBox="0 0 20 26" aria-hidden="true"><path d="M10 0C4.5 0 0 4.4 0 9.8 0 17 10 26 10 26s10-9 10-16.2C20 4.4 15.5 0 10 0zm0 13.5a3.7 3.7 0 1 1 0-7.4 3.7 3.7 0 0 1 0 7.4z" fill="var(--white)"/></svg>
      <div>418 Larkspur Avenue 2nd Cross,<br>Eastmere Park, Riverton-560210</div>
    </div>
    <div class="page-url">www.brighthollow.com</div>
  </section>
</main>
</body>
</html>
```